Non-profit organization requires InDesign based template for a educational booklet

***Overview***
Our business "The Coastal Brightpath Centre for Skills and Learning" is a not for profit organisation working in vocational education both in the Australian and international markets. While we work within many professional contexts, we also work with projects in developing countries assisting to build institutional capacity in the education industry, upskilling in disadvantaged communities to ultimately facilitate positive development outcomes.

Our project is looking to deliver agricultural-based education units that will be delivered in booklet form. Vocational students will use these unit booklets for self-paced or classroom group study. The front of each unit will have a nice graphical cover page, contents and details about learning in the unit. This will be followed by about 15 pages of educational content with plenty of pictures and other material such as tables and graphs to illustrate learning points. This will then be followed by a short question sheet with space for students to write answers, followed by Activity sheets where students put into practice skills from the unit.

***The designed template should have***
* Cover page;
* Content page;
* Two (2) different introduction pages (two for variation);
* Three (3) different pages for lesson text – these pages will be the main study pages for the students, 3 for variation;
* Activity page - like an activity worksheet;
* Question page - page with questions or reflections that the students need to answer - a space under each question for students to write;

***Design preferences***

*Font – an inDesign default font please like Calibri – text built on a base Normal font 11pt, then headings H1, H2 etc... from that basis e.g. 24pt for H1 etc... the size up to the designer.

Happy to see creativity of graphic artists with the above themes.

Target Market(s)

In the requested project, I require an Adobe InDesign template (file in .indd) to be designed that will have particular characteristics suited to students who are:

* Age 15-17;
* Have the educational equivalent to Australian and US education standard of Yr 8;
* Attending vocational school - vocational schools are between secondary high school and University and are usually used to produce graduates within the skill trade area;
* Agricultural theme in the template;
* Sustainability theme (agricultural sustainability) as well;

Students are from very poor rural farming families in growing rice, coconut, rambutan, mangoes, cocoa, palm oil... - very SE Asian agricultural landscape.

Students are used to black and white government textbooks which are very dry, largely dull in design and colour – we do not want this!

Industry/Entity Type

Agriculture

Font styles to use
Sans Serif

Colors

Designer to choose colors to be used in the design.

Requirements
Must have
• * Final file must be in an editable Adobe Indesign file (.indd), with editable layers;
• * SE Asian agricultural theme in the template;
• * design must not look like dull and boring textbooks or corporate training booklets; * design should be vibrant and interesting but also not distracting from the lesson (i.e. it is not too garish);
• * suitable colours (it will be printed full colour) easy on the eye for students of the age group - colours related to agriculture;
• *Modern look and feel;
Should not have
• * design must not look like dull and boring textbooks or corporate training booklets;

```html
<!DOCTYPE html>
<html lang="en">
<head>
<meta charset="utf-8">
<title>Lesson Spread</title>
<link rel="stylesheet" href="https://fonts.googleapis.com/css2?family=Carlito:wght@400;700&display=swap">
<style>
  :root {
    --backdrop: #d8cfca;
    --paper: #ffffff;
    --ink: #3d3a37;
    --ink-soft: #5a5652;
    --harvest: #e6a93b;
    --straw: #f2c76e;
    --terrace-light: #c9a56a;
    --terrace-dark: #6f5a38;
    --grain-light: #e7b85a;
    --grain-dark: #8a6a3a;
  }
  * { box-sizing: border-box; margin: 0; padding: 0; }
  html, body {
    width: 1200px; height: 833px; overflow: hidden;
    background: var(--backdrop);
    font-family: "Carlito", "Calibri", sans-serif;
    color: var(--ink);
  }
  .spread {
    position: absolute; left: 48px; top: 26px;
    width: 1104px; height: 780px;
    display: flex;
    box-shadow: 0 10px 30px rgba(60, 40, 30, .18);
  }
  .page {
    position: relative; width: 552px; height: 780px;
    background: var(--paper);
  }
  .page--left { box-shadow: inset -14px 0 18px -14px rgba(0,0,0,.18); }
  .page--right { box-shadow: inset 14px 0 18px -14px rgba(0,0,0,.14); }

  /* left page */
  .hero-image { position: absolute; left: 36px; top: 40px; width: 484px; height: 340px; }
  .lesson-title {
    position: absolute; left: 40px; top: 368px;
    font-size: 30px; font-weight: 700; color: var(--harvest); letter-spacing: .5px;
  }
  .lesson-intro {
    position: absolute; left: 40px; top: 410px; width: 472px;
    font-size: 16.5px; line-height: 1.28; color: var(--ink-soft);
  }
  .body-columns {
    position: absolute; display: flex; gap: 22px;
    font-size: 10px; line-height: 1.42; color: var(--ink);
  }
  .body-columns p + p { margin-top: 8px; }
  .page--left .body-columns { left: 40px; top: 520px; width: 472px; }
  .page--left .body-columns .column { flex: 1; }

  /* right page */
  .facts-box {
    position: absolute; left: 34px; top: 40px; width: 270px; height: 215px;
    background: var(--straw); padding: 22px 24px; color: var(--paper);
  }
  .facts-box h2 { font-size: 22px; font-weight: 700; margin-bottom: 8px; }
  .facts-box p { font-size: 10.5px; line-height: 1.4; }
  .facts-box p + p { margin-top: 9px; }
  .grain-image { position: absolute; left: 304px; top: 40px; width: 216px; height: 150px; }
  .column--facts-side { position: absolute; left: 40px; top: 275px; width: 228px; }
  .column--photo-side { position: absolute; left: 292px; top: 206px; width: 228px; }
  .page--right .column { font-size: 10px; line-height: 1.45; }
  .page--right .column p + p { margin-top: 8px; }
</style>
</head>
<body>
<main class="spread">
  <section class="page page--left">
    <svg class="hero-image" viewBox="0 0 484 340" role="img" aria-label="Photograph of terraced rice fields on a hillside with a small wooden farm hut">
      <defs>
        <linearGradient id="terraceTone" x1="0" y1="0" x2="1" y2="1">
          <stop offset="0" stop-color="var(--terrace-dark)"/>
          <stop offset=".5" stop-color="var(--terrace-light)"/>
          <stop offset="1" stop-color="#b48f55"/>
        </linearGradient>
      </defs>
      <path d="M0 0 H484 V250 Q300 280 0 340 Z" fill="url(#terraceTone)"/>
    </svg>
    <h1 class="lesson-title">Leson text</h1>
    <p class="lesson-intro">Qui ut dolectiur, sunt dersperum non cullupt aepudit pro mil in re velibus maximolorem faccupi tiberit que eumquo voluptati que eium utenist ionsequat re quam derum idebit vent et pelection conest rem-pero consed quibus verundam facestore plis mo es exerum hil ex est assedip itaquia</p>
    <div class="body-columns">
      <div class="column">
        <p>Rice terraces follow the natural shape of the hill. Each level holds water after rain and slows the flow of soil down the slope. Farmers repair the small walls before planting so the fields stay flat and wet. This careful work protects the land for the next season and for the next family.</p>
      </div>
      <div class="column">
        <p>Look at the hillside and count the levels you can see. Think about how water moves from the top field to the lowest one. Why do you think the walls are made from mud and stones? Write your ideas in your notebook before you read the next page.</p>
      </div>
    </div>
  </section>

  <section class="page page--right">
    <aside class="facts-box">
      <h2>Facts</h2>
      <p>Ti tem esti omnolore, solupta ecescium quias ipietur sinitius. Um dolupta dolor susandis nostem eatus autesto berias re que comnias erciate</p>
      <p>Ti tem esti omnolore, solupta ecescium quias ipietur sinitius. Um dolupta dolor susandis nostem eatus autesto berias re que comnias erciate</p>
      <p>Ti tem esti omnolore, solupta ecescium quias ipietur sinitius.</p>
    </aside>
    <svg class="grain-image" viewBox="0 0 216 150" role="img" aria-label="Photograph of a hand holding ripe golden rice grains">
      <defs>
        <linearGradient id="grainTone" x1="0" y1="0" x2="1" y2="1">
          <stop offset="0" stop-color="var(--grain-dark)"/>
          <stop offset=".45" stop-color="var(--grain-light)"/>
          <stop offset="1" stop-color="#c98f4a"/>
        </linearGradient>
      </defs>
      <rect width="216" height="150" fill="url(#grainTone)"/>
    </svg>
    <div class="column column--facts-side">
      <p>Healthy soil is the start of every good harvest. Soil is full of tiny living things that break down old leaves and straw. These living things feed the plants we grow. When we burn straw or leave the ground bare, we lose this food and the soil becomes weak.</p>
      <p>A better way is to return the straw to the field. Cut it into short pieces and mix it into the mud before the next planting. Over time the soil turns darker and holds more water. Plants grow stronger roots and need less fertiliser from the shop.</p>
      <p>Compost is another simple tool. Pile up coconut husks, mango leaves, rice straw and animal manure in a shady corner. Turn the pile every week and keep it damp. After two or three months it becomes soft, dark and sweet smelling. Spread it around young trees and vegetables.</p>
    </div>
    <div class="column column--photo-side">
      <p>Water is the second key to a strong crop. Rice needs standing water for most of its life, but not all of the time. Letting the field dry for a few days in the middle of the season helps the roots grow deep and saves water for other farms downstream.</p>
      <p>Check the channels at the edge of each terrace after heavy rain. Clear away fallen branches and rubbish so water can move freely. A blocked channel can break a wall and wash away a whole field.</p>
      <p>Finally, talk with older farmers in your village. They have watched the same fields for many years. Ask them which methods work best in dry years and in wet years, and share what you learn with your class.</p>
    </div>
  </section>
</main>
</body>
</html>
```